Startup Drone Platform Company business card

We are needing a business card design for our employees. We are a startup drone platform. We are looking for a business card that has our logo on one side, with the employee/company details on the opposite side. We are looking for something that is very eye catching, modern, and bold.

Target Market(s)

This will target both drone pilots and drone businesses, along with all the industries that could utilize drone services (aerial video, aerial photos, inspections, 3d mapping, etc).

Industry/Entity Type

Business

```html
<!DOCTYPE html>
<html lang="en">
<head>
<meta charset="utf-8">
<title>Skylane Aerial – Business Card</title>
<link rel="stylesheet" href="https://fonts.googleapis.com/css2?family=Lato:wght@400;700&display=swap">
<style>
  :root {
    --backdrop: #eeeeee;
    --card: #0b0d0d;
    --white: #f2f4f4;
    --detail: #7fa3ab;
    --teal-bright: #3bc0cb;
    --teal-mid: #226f7a;
    --teal-deep: #13292e;
  }
  * { margin: 0; padding: 0; box-sizing: border-box; }
  html, body {
    width: 1200px;
    height: 800px;
    overflow: hidden;
    background: var(--backdrop);
    font-family: "Lato", sans-serif;
  }
  .sheet {
    width: 1200px;
    height: 800px;
    display: flex;
    align-items: center;
    justify-content: center;
    gap: 80px;
  }
  .card {
    position: relative;
    width: 460px;
    height: 262px;
    background: var(--card);
    overflow: hidden;
  }

  /* Front */
  .card-front {
    display: flex;
    flex-direction: column;
    align-items: center;
    justify-content: center;
    color: var(--white);
  }
  .brand-dot {
    width: 38px;
    height: 38px;
    border-radius: 50%;
    background: var(--teal-bright);
    margin-bottom: 22px;
  }
  .brand-name {
    font-weight: 400;
    font-size: 26px;
    letter-spacing: 0.42em;
    padding-left: 0.42em;
    text-transform: uppercase;
  }
  .brand-sub {
    margin-top: 6px;
    font-weight: 400;
    font-size: 12px;
    letter-spacing: 0.5em;
    padding-left: 0.5em;
    text-transform: uppercase;
  }

  /* Back */
  .corner-glow {
    position: absolute;
    left: 0;
    top: 0;
    width: 460px;
    height: 262px;
    background: radial-gradient(circle at 0% 100%,
      var(--teal-bright) 0%,
      var(--teal-mid) 30%,
      var(--teal-deep) 55%,
      rgba(11, 13, 13, 0) 75%);
  }
  .contact {
    position: absolute;
    top: 30px;
    right: 32px;
    text-align: right;
    list-style: none;
    color: var(--detail);
    font-weight: 700;
    font-size: 15px;
    line-height: 1.3;
  }
  .back-mark {
    position: absolute;
    right: 32px;
    bottom: 28px;
    display: flex;
    align-items: center;
    gap: 12px;
    color: var(--white);
    font-size: 11px;
    letter-spacing: 0.45em;
    text-transform: uppercase;
  }
  .back-mark .dot {
    width: 9px;
    height: 9px;
    border-radius: 50%;
    background: var(--teal-bright);
  }
</style>
</head>
<body>
  <main class="sheet">
    <section class="card card-front" aria-label="Card front">
      <span class="brand-dot"></span>
      <p class="brand-name">Skylane</p>
      <p class="brand-sub">Aerial</p>
    </section>

    <section class="card card-back" aria-label="Card back">
      <div class="corner-glow" role="img" aria-label="Decorative teal graphic rising from the lower left corner"></div>
      <ul class="contact">
        <li>Skylane Aerial</li>
        <li>Your Address</li>
        <li>Telephone Number</li>
        <li>Email</li>
        <li>Web Address</li>
      </ul>
      <p class="back-mark"><span>Skylane</span><span class="dot"></span><span>Aerial</span></p>
    </section>
  </main>
</body>
</html>
```